Project Managers Business card design

We need business cards for our Project Managers based in Sydney for our business name Korbet Pty Ltd. We project manage property improvements and infrastructure Assets. We provide asset owners Project Management services from original concept, management of architectural and engineering designs, call and select construction tenders, and manage the Asset operational life cycle to conclusion and removal. We are experienced in feasibility studies, risk assessments, quality control, safety control, environmental analysis. We are specialist in Aged Care and Child Care Services. We can provide asset reviewing checklists, asset inspections, contract cost and contract assessments, dispute resolution services and articles and books on safely working and living in environments subject to analysis. the design colours should be queensland marone and NSW sky blue.

Industry/Entity Type

Construction

Contact Information for Business Card

Dennis Marlow (Mb 0402 781954), Gavin Trelford (Mb 0438 216 047), Len Obradin,(Mb 0427 863 105)
E: all business cards: korbet@mailnest.example
Office phone number (02) 9482 3061
Address
Level 1 Harwell Building
47 Fenwick Street, Parramatta
Web: projectmanagers@estateleadsbykorbet.example (to be checked on Printwell web draft)

```html
<!DOCTYPE html>
<html lang="en">
<head>
<meta charset="utf-8">
<title>Korbet Pty Ltd – Business Cards</title>
<link rel="stylesheet" href="https://fonts.googleapis.com/css2?family=Cinzel:wght@700&family=Play:wght@400;700&family=Ubuntu:ital,wght@1,400;1,700&display=swap">
<style>
  :root {
    --backdrop: #a3a3a1;
    --paper: #f3f3f1;
    --maroon: #73182c;
    --sky: #6cace4;
    --ink: #353535;
    --ink-soft: #4a4a4a;
    --on-band: #f6f4f2;
  }
  * { box-sizing: border-box; margin: 0; padding: 0; }
  html, body { width: 1200px; height: 1000px; overflow: hidden; }
  body { background: var(--backdrop); position: relative; font-family: "Play", sans-serif; }

  .card {
    position: absolute;
    background: var(--paper);
    overflow: hidden;
    box-shadow: 0 6px 18px rgba(0,0,0,0.25);
  }

  /* Back of card */
  .card--back { left: 440px; top: 60px; width: 680px; height: 388px; }
  .card--back .brand-band {
    position: absolute; left: 0; right: 0; top: 120px; height: 150px;
    background: var(--maroon);
    border-top: 6px solid var(--sky);
    border-bottom: 6px solid var(--sky);
    display: flex; align-items: center; justify-content: center;
  }
  .brand-name {
    font-family: "Cinzel", serif; font-weight: 700;
    color: var(--on-band); letter-spacing: 0.04em; white-space: nowrap;
  }
  .card--back .brand-name { font-size: 52px; }

  /* Front of card */
  .card--front { left: 80px; top: 500px; width: 740px; height: 423px; }
  .front-top-band { position: absolute; left: 0; right: 0; top: 0; height: 40px; background: var(--sky); }
  .front-brand-band {
    position: absolute; left: 0; right: 0; top: 82px; height: 62px;
    background: var(--maroon);
    display: flex; align-items: center; justify-content: center;
  }
  .card--front .brand-name { font-size: 30px; }

  .person {
    position: absolute; left: 0; right: 0; top: 148px; height: 76px;
    display: flex; align-items: center; justify-content: center; gap: 22px;
  }
  .person .rule { flex: 1; height: 5px; background: var(--sky); }
  .person-text { text-align: center; color: var(--ink); font-family: "Ubuntu", sans-serif; font-style: italic; }
  .person-name { font-size: 28px; font-weight: 700; line-height: 1.1; color: var(--maroon); }
  .person-role { font-size: 16px; font-weight: 400; color: var(--ink-soft); }

  .contact-block {
    position: absolute; left: 0; right: 0; top: 228px; bottom: 0;
    background: var(--maroon); color: var(--on-band);
    border-top: 5px solid var(--sky);
    display: flex; flex-direction: column; align-items: center; justify-content: center;
    gap: 3px; text-align: center; padding: 0 16px;
  }
  .contact-line { font-size: 21px; line-height: 1.2; white-space: nowrap; }
  .contact-line .gap { display: inline-block; width: 36px; }
  .contact-note { font-size: 19px; }
  .contact-address { font-size: 24px; margin-top: 4px; }
</style>
</head>
<body>
  <section class="card card--back" aria-label="Business card, back">
    <div class="brand-band"><span class="brand-name">Korbet Pty Ltd</span></div>
  </section>

  <section class="card card--front" aria-label="Business card, front">
    <div class="front-top-band"></div>
    <div class="front-brand-band"><span class="brand-name">Korbet Pty Ltd</span></div>
    <div class="person">
      <span class="rule"></span>
      <div class="person-text">
        <p class="person-name">Len Obradin</p>
        <p class="person-role">Project Manager</p>
      </div>
      <span class="rule"></span>
    </div>
    <div class="contact-block">
      <p class="contact-line">M : 0427- 863- 105<span class="gap"></span>O : (02) 9482- 3061</p>
      <p class="contact-line">E : korbet@mailnest.example</p>
      <p class="contact-line">W : projectmanagers@estateleadsbykorbet.example</p>
      <p class="contact-line contact-note">(to be checked on Printwell web draft)</p>
      <p class="contact-line contact-address">Level 1 Harwell Building 47 Fenwick Street, Parramatta</p>
    </div>
  </section>
</body>
</html>
```